brookline diner & tap

menu design contracting menu to two views. reducing number of offerings. website. http://brooklinediner-ferrowave.com/brooklinemenu.html
have reduced our menu offering by 25 items to achieve a 2 view profile vs our current 5 view look. 8 1/2 x 11 preferred but 8 1/2 by 14 possible. Would like to employ a menu board concept but sleeves will also be a considered option.

Target Market(s)

families, blue collar, home style, meat loaf, fried chicken, burgers, chicken fried steak etc

Industry/Entity Type

American Restaurant

Font styles to use
Sans Serif

Colors
f68e4d
faa54b
fece3e
fbee3e
aaaaaa
9d9d9d
b1b1b1
1b1b1b

Requirements
Must have
• 2 views
Nice to have
• colors
Should not have
• clutter, unstructured,

```html
<!DOCTYPE html>
<html lang="en">
<head>
<meta charset="utf-8">
<title>Brookline Diner &amp; Tap — Menu</title>
<link rel="stylesheet" href="https://fonts.googleapis.com/css2?family=Archivo+Black&family=Roboto+Condensed:wght@400;700&display=swap">
<style>
  :root {
    --paper: #ecdfc6;
    --paper-edge: #d9c7a6;
    --red: #b3262c;
    --ink: #2b2420;
    --band-text: #f4e9d6;
    --art-warm: #c8955c;
    --art-light: #efe3cc;
  }
  * { box-sizing: border-box; margin: 0; padding: 0; }
  html, body { width: 928px; height: 1200px; overflow: hidden; }
  body {
    position: relative;
    background: radial-gradient(ellipse at 50% 45%, #f1e6d0 0%, var(--paper) 55%, var(--paper-edge) 100%);
    font-family: "Roboto Condensed", sans-serif;
    color: var(--ink);
  }
  .brand {
    position: absolute; top: 62px; left: 0; width: 928px;
    text-align: center;
    font-family: "Roboto Condensed", sans-serif;
    font-weight: 700; font-size: 34px; color: var(--red);
    letter-spacing: 1px;
  }
  .section-title {
    position: absolute; left: 0; width: 928px; text-align: center;
    font-family: "Archivo Black", sans-serif;
    color: var(--red); font-size: 44px; letter-spacing: 6px;
  }
  .section-title.appetizers { top: 160px; }
  .column { position: absolute; }
  .item { margin-bottom: 15px; }
  .item-head {
    display: flex; justify-content: space-between;
    color: var(--red); font-weight: 700; font-size: 16px; line-height: 18px;
  }
  .item-desc { font-size: 13.4px; line-height: 15px; text-transform: uppercase; }
  .item-desc ul { list-style: none; padding-left: 10px; }
  .item-desc li::before { content: "• "; }
  .apps-left { top: 226px; left: 58px; width: 376px; }
  .apps-right { top: 226px; left: 480px; width: 386px; }

  .burgers-frame {
    position: absolute; top: 592px; left: 30px; width: 870px; height: 472px;
    border: 1.5px solid var(--red); border-top: none;
  }
  .burgers-band {
    position: absolute; top: 592px; left: 30px; width: 870px; height: 58px;
    background: var(--red);
  }
  .burgers-band h2 {
    position: absolute; left: 14px; top: 6px;
    font-family: "Archivo Black", sans-serif; font-weight: 400;
    font-size: 40px; letter-spacing: 5px; color: var(--band-text);
  }
  .burger-art {
    position: absolute; top: 528px; left: 512px; width: 396px; height: 290px;
  }
  .burgers-left { top: 686px; left: 58px; width: 376px; }
  .burgers-right { top: 826px; left: 480px; width: 386px; }

  .footer-prices {
    position: absolute; top: 1080px; left: 0; width: 928px; text-align: center;
    font-family: "Archivo Black", sans-serif; color: var(--red);
    font-size: 19px; letter-spacing: 2px;
  }
  .footer-note {
    position: absolute; top: 1104px; left: 0; width: 928px; text-align: center;
    font-size: 22px; letter-spacing: 1.5px; text-transform: uppercase;
  }
  .advisory {
    position: absolute; top: 1158px; left: 40px; width: 848px; text-align: center;
    font-size: 10.5px; line-height: 13px; text-transform: uppercase;
  }
</style>
</head>
<body>
  <div class="brand">brookline diner &amp; tap</div>

  <h1 class="section-title appetizers">APPETIZERS</h1>

  <div class="column apps-left">
    <div class="item"><div class="item-head"><span>FRIED MOZZARELLA CHEESE STIX</span><span>$7.99</span></div>
      <p class="item-desc">Served with marinara sauce</p></div>
    <div class="item"><div class="item-head"><span>FRIED PICKLES!</span><span>$7.99</span></div>
      <p class="item-desc">Hand breaded and fried with ranch<br>dipping sauce</p></div>
    <div class="item"><div class="item-head"><span>ONION RING TOWER!</span><span>$7.99</span></div>
      <p class="item-desc">Romine heart, caesar vinaigrette, sous-vide<br>egg yolk, bacon, parmesan, crostini, smoked lime.</p></div>
    <div class="item"><div class="item-head"><span>“TEXAS STYLE” CHICKEN FRIED BACON</span><span>$7.99</span></div>
      <p class="item-desc">Straight from the heart of Texas, hand<br>breaded &amp; deep fried hickory smoked bacon,<br>served with country gravy for dippin’!<br>You’ll love it!</p></div>
    <div class="item"><div class="item-head"><span>CHEDDAR POTATO BOATS!</span><span>$7.99</span></div>
      <p class="item-desc">Fried potato skins, loaded with cheddar &amp; mozza-<br>rella cheese, bacon, fried onion tanglers &amp; driz-<br>zled with buffalo BBQ sauce!</p></div>
  </div>

  <div class="column apps-right">
    <div class="item"><div class="item-head"><span>FLAT BREAD PIZZA</span><span>$10.99</span></div>
      <div class="item-desc">12” &amp; we’ll top it the way you like!
        <ul><li>Pepperoni &amp; sausage, cheese</li><li>All veggie &amp; cheese</li><li>Cheese</li><li>Chicken ranch</li><li>Supreme</li></ul></div></div>
    <div class="item"><div class="item-head"><span>MACHO NACHO PLATTER</span><span>$8.99</span></div>
      <p class="item-desc">We load this platter with refried beans, taco meat,<br>chili, salsa, jack, cheddar, &amp; mozzarella cheeses, let-<br>tuce, tomato, jalapeños, sour cream &amp; tri-colored<br>corn chips! (Small 7.99)</p></div>
    <div class="item"><div class="item-head"><span>FRIED JALAPEÑOS</span><span>$7.99</span></div>
      <p class="item-desc">Baby octopus tentacle, baby clams, mussels,<br>scallop, bouillabaisse, white corn grits.</p></div>
  </div>

  <div class="burgers-frame"></div>
  <div class="burgers-band"><h2>GOURMET BURGERS</h2></div>

  <svg class="burger-art" viewBox="0 0 396 290" role="img" aria-label="Illustration of two stacked gourmet burgers with fries">
    <defs>
      <radialGradient id="artTone" cx="50%" cy="55%" r="60%">
        <stop offset="0%" stop-color="var(--art-warm)"/>
        <stop offset="100%" stop-color="var(--art-light)" stop-opacity="0"/>
      </radialGradient>
    </defs>
    <rect width="396" height="290" fill="url(#artTone)"/>
  </svg>

  <div class="column burgers-left">
    <div class="item"><div class="item-head"><span>BACON CHEDDAR CHEESE BURGER</span><span>$8.99</span></div>
      <p class="item-desc">Half pound burger with melting cheddar<br>cheese &amp; crispy bacon!</p></div>
    <div class="item"><div class="item-head"><span>SWISS MUSHROOM BACON BURGER</span><span>$8.99</span></div>
      <p class="item-desc">Melting swiss cheese, sauteed mushrooms &amp;<br>crispy bacon!</p></div>
    <div class="item"><div class="item-head"><span>BLUE CHEESE BACON AVOCADO</span><span>$8.99</span></div>
      <p class="item-desc">Half pound patty topped with blue cheese crumbles,<br>crisp bacon, avocado slices &amp; honey mustard sauce</p></div>
    <div class="item"><div class="item-head"><span>THE “ULTIMATE BURGER”</span><span>$8.99</span></div>
      <p class="item-desc">Here we go! A half pound patty topped with<br>provolone cheese, crisp bacon, pastrami, sauteed<br>mushrooms &amp; onions, jalapeños &amp; fried onion<br>tanglers! You’ll love it!</p></div>
    <div class="item"><div class="item-head"><span>“D’EST BURGER”</span><span>$8.99</span></div>
      <p class="item-desc">Ground sirloin patty topped with cheddar cheese,<br>hickory smoked ham, more cheese &amp; crisp bacon</p></div>
  </div>

  <div class="column burgers-right">
    <div class="item"><div class="item-head"><span>“THE DOUBLER”</span><span>$10.99</span></div>
      <p class="item-desc">Double the patties, double the cheese (cheddar and<br>provolone), double the bacon!</p></div>
    <div class="item"><div class="item-head"><span>RANCH HOUSE BURGER</span><span>$8.99</span></div>
      <p class="item-desc">Half pound burger topped with cheddar cheese,<br>a fried egg &amp; crisp bacon</p></div>
    <div class="item"><div class="item-head"><span>GREAT WESTERN</span><span>$8.99</span></div>
      <p class="item-desc">America’s favorite burger! Ground sirloin, topped<br>with cheddar cheese, crisp bacon, onion rings &amp;<br>BBQ sauce</p></div>
  </div>

  <div class="footer-prices">HAMBURGER 6.99 // CHEESEBURGER 7.99</div>
  <div class="footer-note">All burgers served with bottle neck french fries</div>
  <p class="advisory">Consumer advisory: consuming raw or undercooked meat, poultry, seafood, shellfish or eggs may increase your risk of foodborne illness.<br>Sorry, we can’t split small portions. Split order will be charged small portion price or ½ price plus $1 per person if small portion not offered.</p>
</body>
</html>
```